Design for mobile and web app for sweepstakes.

We need the design for a mobile app (planned to be build with jquery mobile) and web app (mobile first, we will use same look and feel as mobile just with displaying more info at once).

The following pages must be included:
- Userregistration/Login (Reg via Email, Chatnook-Reg)

- List of available sweepstakes (including some icons: a video icon, a "like button" type icon, a "provide some info" type of icon) this should be on the side in wep app but in mobile app its a list. possible is also a mobile display where users can swipe back and forth through it.

- single sweepstake detailview . should present a single sweepstake and give users the opportunity to participate with a button.

user settings. (doesnt not have to include a lot of fields we will at ourself. should contain some datepicker (birthday), some on/off switch (receive newsletters) some textfield in order for us to have a feel.

We have included the following files:
- prizewell_logo_final01.png:
this is our logo which should be used and also the look and feel must fit with the logo.

- prizewell_logo_final06.png:
this is the app-icon

this is a simple mockup for a registration page. the design doesnt have to contain all fields we will do that ourselfes starting from your handover, but should represent a common registration page with some fields

this is just a mockup for a possible design. not that it does use our old logo. This again is not binding is just to get a feel for what we are looking for. A list of sweepstakes and a detailspage for the sweepstake for users to participate in it.

Target Market(s)

German speaking users, Austria, Germany, Switzerland
The app is adressing a wide crowd of users who are interested in participating in sweepstakes.

Industry/Entity Type

Build

Number of Pages Required

4 page

Font styles to use
Sans Serif

Requirements
Must have
• - jquery and jquery mobile
• - html5 (preferable bootstrap-based)
• - css3
• - description on used fonts and colors. fonts must be free to use and publicly available for anyone to use.
• - all buttons should be css

```html
<!DOCTYPE html>
<html lang="en">
<head>
<meta charset="utf-8">
<title>prizewell – Sweepstakes</title>
<link rel="stylesheet" href="https://fonts.googleapis.com/css2?family=Arimo:wght@400;700&display=swap">
<style>
  :root {
    --gold-light: #e3d795;
    --gold-mid: #d2c37a;
    --gold-deep: #b9a55c;
    --brand-green: #5f9e2c;
    --icon-green: #6ea33a;
    --accent-yellow: #f8bb06;
    --button-green: #8cc314;
    --button-yellow: #ffc20e;
    --title-grey: #6b6548;
    --body-grey: #8a8a8a;
    --white: #ffffff;
    --divider: rgba(255, 255, 240, 0.45);
  }
  * { box-sizing: border-box; margin: 0; padding: 0; }
  html, body {
    width: 1200px;
    height: 2521px;
    overflow: hidden;
  }
  body {
    font-family: "Arimo", Arial, sans-serif;
    background:
      radial-gradient(ellipse 700px 500px at 45% 12%, rgba(255, 250, 210, 0.55), transparent 70%),
      radial-gradient(ellipse 600px 700px at 80% 55%, rgba(255, 248, 200, 0.35), transparent 70%),
      linear-gradient(160deg, var(--gold-mid) 0%, var(--gold-light) 45%, var(--gold-mid) 75%, var(--gold-deep) 100%);
    position: relative;
  }
  .app-header {
    height: 260px;
    display: flex;
    align-items: center;
    justify-content: center;
    gap: 22px;
  }
  .brand-dot {
    width: 54px;
    height: 54px;
    border-radius: 50%;
    background: var(--brand-green);
  }
  .brand-name {
    font-size: 64px;
    font-weight: 700;
    color: var(--brand-green);
    letter-spacing: -1px;
  }
  .sweepstake-list {
    list-style: none;
    padding: 0 30px 0 30px;
  }
  .sweepstake-item {
    height: 318px;
    display: flex;
    align-items: center;
    justify-content: space-between;
    padding: 0 0 0 8px;
    border-bottom: 3px solid var(--divider);
  }
  .sweepstake-item.is-active {
    background: var(--white);
    margin: 0 -13px;
    padding: 0 25px 0 20px;
    border-bottom: none;
    height: 300px;
    margin-bottom: 18px;
  }
  .item-text { width: 960px; }
  .item-title {
    font-size: 31px;
    font-weight: 700;
    color: var(--title-grey);
    text-transform: uppercase;
    margin-bottom: 26px;
  }
  .item-desc {
    font-size: 27px;
    line-height: 50px;
    color: var(--white);
  }
  .is-active .item-title { color: var(--accent-yellow); }
  .is-active .item-desc { color: var(--body-grey); }
  .item-date { color: var(--accent-yellow); }
  .item-icon {
    width: 96px;
    height: 96px;
    border-radius: 50%;
    background: var(--icon-green);
    display: flex;
    align-items: center;
    justify-content: center;
    flex-shrink: 0;
    margin-right: 12px;
  }
  .is-active .item-icon { background: var(--accent-yellow); }
  .item-icon svg { width: 48px; height: 48px; fill: var(--white); }
  .actions {
    display: flex;
    justify-content: center;
    gap: 44px;
    margin-top: 118px;
  }
  .btn {
    width: 388px;
    height: 110px;
    border: 2px solid rgba(0, 0, 0, 0.08);
    border-radius: 3px;
    font-family: inherit;
    font-size: 44px;
    font-weight: 700;
    color: var(--white);
    text-transform: uppercase;
  }
  .btn-learn { background: var(--button-green); }
  .btn-view { background: var(--button-yellow); }
</style>
</head>
<body>
  <header class="app-header">
    <span class="brand-dot"></span>
    <span class="brand-name">prizewell</span>
  </header>

  <ul class="sweepstake-list">
    <li class="sweepstake-item is-active">
      <div class="item-text">
        <h2 class="item-title">Neque porro quisquam est</h2>
        <p class="item-desc">It is a long established fact that a reader will be distracted by the readable content of a page when looking at its layout..........<span class="item-date">23-12 -2014</span></p>
      </div>
      <span class="item-icon">
        <svg viewBox="0 0 24 24" aria-hidden="true"><path d="M12 3 1.5 12.5h3V21h6v-6h3v6h6v-8.5h3z"/></svg>
      </span>
    </li>
    <li class="sweepstake-item">
      <div class="item-text">
        <h2 class="item-title">Neque porro quisquam est</h2>
        <p class="item-desc">It is a long established fact that a reader will be distracted by the readable content of a page when looking at its layout.</p>
      </div>
      <span class="item-icon">
        <svg viewBox="0 0 24 24" aria-hidden="true"><rect x="1" y="6" width="15" height="12" rx="2"/><path d="M17 10.5 23 6.5v11l-6-4z"/></svg>
      </span>
    </li>
    <li class="sweepstake-item">
      <div class="item-text">
        <h2 class="item-title">Neque porro quisquam est</h2>
        <p class="item-desc">It is a long established fact that a reader will be distracted by the readable content of a page when looking at its layout.</p>
      </div>
      <span class="item-icon">
        <svg viewBox="0 0 24 24" aria-hidden="true"><rect x="1.5" y="10" width="4.5" height="11" rx="1"/><path d="M7.5 10.5 12 3c1.6 0 2.6 1 2.2 2.8L13.5 9h6.3c1.3 0 2.2 1.2 1.9 2.4l-1.9 7.9c-.3 1-1.1 1.7-2.1 1.7H7.5z"/></svg>
      </span>
    </li>
    <li class="sweepstake-item">
      <div class="item-text">
        <h2 class="item-title">Neque porro quisquam est</h2>
        <p class="item-desc">It is a long established fact that a reader will be distracted by the readable content of a page when looking at its layout.</p>
      </div>
      <span class="item-icon">
        <svg viewBox="0 0 24 24" aria-hidden="true"><rect x="1" y="6" width="15" height="12" rx="2"/><path d="M17 10.5 23 6.5v11l-6-4z"/></svg>
      </span>
    </li>
    <li class="sweepstake-item">
      <div class="item-text">
        <h2 class="item-title">Neque porro quisquam est</h2>
        <p class="item-desc">It is a long established fact that a reader will be distracted by the readable content of a page when looking at its layout.</p>
      </div>
      <span class="item-icon">
        <svg viewBox="0 0 24 24" aria-hidden="true"><path d="M12 3 1.5 12.5h3V21h6v-6h3v6h6v-8.5h3z"/></svg>
      </span>
    </li>
    <li class="sweepstake-item">
      <div class="item-text">
        <h2 class="item-title">Neque porro quisquam est</h2>
        <p class="item-desc">It is a long established fact that a reader will be distracted by the readable content of a page when looking at its layout.</p>
      </div>
      <span class="item-icon">
        <svg viewBox="0 0 24 24" aria-hidden="true"><rect x="1.5" y="10" width="4.5" height="11" rx="1"/><path d="M7.5 10.5 12 3c1.6 0 2.6 1 2.2 2.8L13.5 9h6.3c1.3 0 2.2 1.2 1.9 2.4l-1.9 7.9c-.3 1-1.1 1.7-2.1 1.7H7.5z"/></svg>
      </span>
    </li>
  </ul>

  <div class="actions">
    <button class="btn btn-learn" type="button">Learn More</button>
    <button class="btn btn-view" type="button">View More</button>
  </div>
</body>
</html>
```